Executive Performance Review mapped on J-curve

I need to turn an executive company performance review into a visual infographic. The list of accomplishments is grouped into four calendar quarters. Each quarter needs a subtle representation of the season. The four quarters and associated list of accomplishments need to be mapped to a J-curve. - Spreadsheet with accomplishments attached (Throughput)- Sample image of a J-curve. You can google J-curve to see more images.- The title should be "Danela Morsky Year in Review"

Target Market(s)

Board of Directors

Requirements
Nice to have
• This will be presented to a company founder that is an artist and customer experience expert. He is very visual so a nice visual representation of the data will be impactful. He also uses the phrase that you have to live with or work with someone for four seasons before you really know them. This is why I have the seasons mapped to the quarters. The Fall season motif should be gloomy and stormy.

```html
<!DOCTYPE html>
<html lang="en">
<head>
<meta charset="utf-8">
<title>Danela Morsky Year in Review</title>
<link rel="stylesheet" href="https://fonts.googleapis.com/css2?family=Jost:wght@600&family=Source+Sans+3:wght@400;600&family=Arimo&display=swap">
<style>
  :root {
    --summer-bg: #fdf5d6;
    --fall-bg: #f7dcc6;
    --winter-bg: #eefbfd;
    --spring-bg: #eff7df;
    --ink: #1e1e1e;
    --title-yellow: #f9c413;
    --title-orange: #ec8a16;
    --title-tan: #d9b08a;
    --title-blue: #bfe9f8;
    --title-green: #c7e27a;
  }
  html, body {
    margin: 0;
    padding: 0;
    width: 1200px;
    height: 734px;
    overflow: hidden;
    background: #ffffff;
  }
  .canvas {
    position: relative;
    width: 1200px;
    height: 734px;
    font-family: "Source Sans 3", sans-serif;
    color: var(--ink);
  }
  .review-title {
    position: absolute;
    left: 0;
    width: 1110px;
    top: 76px;
    margin: 0;
    text-align: center;
    font-family: "Jost", sans-serif;
    font-weight: 600;
    font-size: 46px;
    letter-spacing: 0.5px;
    background: linear-gradient(90deg, var(--title-yellow) 18%, var(--title-orange) 38%, var(--title-tan) 55%, var(--title-blue) 68%, var(--title-green) 95%);
    -webkit-background-clip: text;
    background-clip: text;
    color: transparent;
    padding-left: 90px;
  }
  .season-band {
    position: absolute;
    top: 144px;
    height: 510px;
    width: 267px;
  }
  .season-band.summer { left: 63px; background: var(--summer-bg); }
  .season-band.fall { left: 330px; width: 266px; background: var(--fall-bg); }
  .season-band.winter { left: 596px; width: 266px; background: var(--winter-bg); }
  .season-band.spring { left: 862px; background: linear-gradient(180deg, #f6faee, var(--spring-bg)); }
  .j-curve {
    position: absolute;
    left: 0;
    top: 0;
  }
  .quarter-notes {
    position: absolute;
    top: 172px;
    font-size: 11.6px;
    line-height: 17px;
  }
  .quarter-notes.summer { left: 71px; width: 258px; }
  .quarter-notes.fall { left: 343px; width: 240px; }
  .quarter-notes.winter { left: 602px; width: 250px; }
  .quarter-notes.spring { left: 872px; width: 250px; }
  .quarter-notes h2 {
    margin: 0 0 0 0;
    font-size: 11.6px;
    font-weight: 600;
    line-height: 17px;
  }
  .quarter-notes ul {
    list-style: none;
    margin: 0 0 4px 0;
    padding: 0;
  }
  .quarter-notes li::before { content: "\2022\00a0"; }
  .quarter-notes li { line-height: 17px; }
  .quarter-notes li.wrap { line-height: 15px; margin: 1px 0 2px; }
  .season-label {
    position: absolute;
    font-family: "Arimo", sans-serif;
    font-size: 14.5px;
    color: #111;
  }
</style>
</head>
<body>
<main class="canvas">
  <h1 class="review-title">DANELA MORSKY YEAR IN REVIEW</h1>

  <div class="season-band summer"></div>
  <div class="season-band fall"></div>
  <div class="season-band winter"></div>
  <div class="season-band spring"></div>

  <svg class="j-curve" width="1200" height="734" viewBox="0 0 1200 734" role="img" aria-label="J-curve rising through the year, filled with seasonal scenes: summer palms and a beach drink, stormy fall leaves and a pumpkin, a winter snowman with snowflakes, and spring flowers with a bee and a bird">
    <defs>
      <linearGradient id="seasonFill" x1="63" y1="0" x2="1129" y2="0" gradientUnits="userSpaceOnUse">
        <stop offset="0" stop-color="#fcc80f"/>
        <stop offset="0.22" stop-color="#f6b112"/>
        <stop offset="0.36" stop-color="#ec861c"/>
        <stop offset="0.49" stop-color="#e98a2e"/>
        <stop offset="0.56" stop-color="#d8e9ee"/>
        <stop offset="0.7" stop-color="#c6ecfa"/>
        <stop offset="0.8" stop-color="#c9edf2"/>
        <stop offset="0.92" stop-color="#c4e063"/>
        <stop offset="1" stop-color="#b7d94c"/>
      </linearGradient>
    </defs>
    <path d="M63 482 C180 532 330 572 460 574 C560 575 700 530 830 460 C960 390 1080 270 1129 148 L1129 654 L63 654 Z" fill="url(#seasonFill)"/>
  </svg>

  <section class="quarter-notes summer">
    <h2>TRANSITIONS</h2>
    <ul>
      <li>RO Transition from Reed &amp; Lina</li>
      <li>Start CR Office Initiative</li>
      <li>Tactical Ops transition from Reed</li>
      <li>Crestline account transition from Omar</li>
    </ul>
    <h2>BIZ ARCHITECTURE</h2>
    <ul>
      <li>Independent Financial Audit</li>
      <li>Organizational Audit - Structure</li>
      <li>Organizational Audit - People</li>
      <li>XF Framework - ESU</li>
      <li>Defined Utilization, Realization, Availability</li>
    </ul>
    <h2>STRATEGY</h2>
    <ul>
      <li>Effective Strategy Meeting</li>
      <li class="wrap">Strategic Themes 2018 - 2020: Stablize, Accelerate, Surge</li>
      <li class="wrap">Business Drivers: Drive Revenue, Improve Norvanite Experience, Increase Brand Awareness</li>
      <li>2 year Managed Services Engagement Model</li>
    </ul>
  </section>

  <section class="quarter-notes fall">
    <h2>BIZ ARCHITECTURE</h2>
    <ul>
      <li class="wrap">XF Framework - Functional Meetings &amp; Scrum of Scrums</li>
      <li>Structured Reorg</li>
      <li>Implemented Reorg</li>
      <li>Quarterly Org Iteration cadence</li>
      <li>Defined Key Hire Plan</li>
      <li>CR Office Operational</li>
      <li>Time Accountability</li>
      <li>Tools ReConfig</li>
      <li>Org Structure v1</li>
    </ul>
    <h2>STRATEGY</h2>
    <ul>
      <li>Norvane QBR - Execs</li>
    </ul>
  </section>

  <section class="quarter-notes winter">
    <h2>BIZ ARCHITECTURE</h2>
    <ul>
      <li>Client QBRs</li>
      <li>XF Framework - Progress Demos</li>
      <li>Org Structure - COE's</li>
      <li>Stablize Accounting &amp; Finance</li>
    </ul>
    <h2>KEY HIRES</h2>
    <ul>
      <li>Controller</li>
      <li>Director CX</li>
    </ul>
    <h2>STRATEGY</h2>
    <ul>
      <li>Founders removed from front line activity</li>
      <li>Norvane QBR - Goal Setting</li>
    </ul>
  </section>

  <section class="quarter-notes spring">
    <h2>Biz Architecture</h2>
    <ul>
      <li>Tiered Pricing Pre-Paid Engagement Model</li>
      <li>XF Framework - Ideation Board</li>
      <li>Consulting Levels &amp; Salary Bands</li>
      <li>Roles &amp; Responsibilities</li>
    </ul>
    <h2>Key Hires</h2>
    <ul>
      <li>Interim HR</li>
      <li>Provisional Client Partner</li>
      <li>Acting Director 1</li>
      <li>Acting Director 2</li>
      <li>Client Partner 1</li>
      <li>Sales Exec 1</li>
    </ul>
  </section>

  <div class="season-label" style="left:65px; top:638px;">Summer: Q3 2018</div>
  <div class="season-label" style="left:332px; top:638px;">Fall: Q4 2018</div>
  <div class="season-label" style="left:598px; top:636px;">Winter: Q1 2019</div>
  <div class="season-label" style="left:866px; top:634px;">Spring: Q2 2019</div>
</main>
</body>
</html>
```